BrookhavenLLC

Real Estate Investment. Buy/Sell house/investment . Trustworthy,Reliable, and friendly

Industry/Entity Type

Real Estate

Contact Information for Business Card

Brookhaven@mailbox-example.com
808-555-0143
Linnea-Joy Patterson

```html
<!DOCTYPE html>
<html lang="en">
<head>
<meta charset="utf-8">
<title>BrookhavenLLC Business Card</title>
<link rel="stylesheet" href="https://fonts.googleapis.com/css2?family=Nunito:wght@400;800&display=swap">
<style>
  :root {
    --backdrop: #e4e6e8;
    --card-blue: #0a7dc1;
    --accent-lime: #a5d20f;
    --text-white: #ffffff;
  }
  * { margin: 0; padding: 0; box-sizing: border-box; }
  html, body {
    width: 1200px;
    height: 1000px;
    overflow: hidden;
    background: var(--backdrop);
  }
  .canvas {
    position: relative;
    width: 1200px;
    height: 1000px;
  }
  .business-card {
    position: absolute;
    left: 75px;
    top: 200px;
    width: 1050px;
    height: 600px;
    background: var(--card-blue);
    overflow: hidden;
    box-shadow: 0 6px 18px rgba(0, 0, 0, 0.18);
  }
  .card-graphics {
    position: absolute;
    inset: 0;
    width: 1050px;
    height: 600px;
  }
  .accent-band { fill: var(--accent-lime); }
  .holder-name,
  .contact-line {
    position: absolute;
    color: var(--text-white);
    white-space: nowrap;
    font-family: "Nunito", sans-serif;
    line-height: 1;
  }
  .holder-name {
    left: 405px;
    top: 148px;
    font-size: 34px;
    font-weight: 800;
    letter-spacing: 0.3px;
  }
  .contact-line {
    font-weight: 400;
    letter-spacing: 0.5px;
  }
  .contact-phone {
    left: 430px;
    top: 352px;
    font-size: 30px;
  }
  .contact-email {
    left: 395px;
    top: 450px;
    font-size: 28px;
  }
</style>
</head>
<body>
  <main class="canvas">
    <section class="business-card" aria-label="BrookhavenLLC business card">
      <svg class="card-graphics" viewBox="0 0 1050 600" aria-hidden="true">
        <polygon class="accent-band band-top" points="404,0 730,0 880,128 316,130"/>
        <polygon class="accent-band band-wide" points="266,205 945,205 1050,300 182,330"/>
        <polygon class="accent-band band-thin" points="128,410 1020,392 1050,398 116,428"/>
        <polygon class="accent-band band-base" points="62,507 990,490 1050,500 1050,600 0,600"/>
      </svg>
      <h1 class="holder-name">Linnea-Joy Patterson</h1>
      <p class="contact-line contact-phone">Phone : 808-555-0143</p>
      <p class="contact-line contact-email">Email : Brookhaven@mailbox-example.com</p>
    </section>
  </main>
</body>
</html>
```